Website for a Psychologist in Private Practice

I need a cool web design for my website: www.drquorvat.com. I would like it to look professional. Keep all the current content and add: Space for video; radio spots (see Velvet Tide Hour Logo below for those); Quick Inquiry; Brindlepost link; 5 star rating on Zunq; a map; reviews from former patients. I am open to suggestions.

Target Market(s)

Those seeking individual and marital counseling.

Industry/Entity Type

Mental Health

Number of Pages Required

1 page

Font styles to use
Sans Serif
Other font styles liked:
• I'm open but no hard to read script

Requirements
Must have
• All the content on my home page with link for video and radio spots. List services and degrees and expertices (pics not necessary).
Nice to have
• A video of me and radio conversations (logo of Velvet Tide Hour radio attached).
Should not have
• Cartoons, comedy, etc.... I don't need pictures of services (marital, depression, etc...) Just list those.

```html
<!DOCTYPE html>
<html lang="en">
<head>
<meta charset="utf-8">
<title>Dr. Marla Q. Quorvat – Psychologist</title>
<link href="https://fonts.googleapis.com/css2?family=Roboto:wght@300;400;500;700&display=swap" rel="stylesheet">
<style>
:root{
  --gold:#c9b04c;
  --gold-dark:#b49a3a;
  --gold-soft:#e9dcaa;
  --ink:#555;
  --ink-light:#888;
  --band:#f1f1f1;
  --white:#fff;
}
*{box-sizing:border-box;margin:0;padding:0}
html,body{width:674px;height:1200px;overflow:hidden;background:var(--white)}
body{font-family:"Roboto",Arial,sans-serif;color:var(--ink);position:relative}
.page{position:relative;width:674px;height:1200px;overflow:hidden}
.abs{position:absolute}

/* top strip */
.top-strip{top:0;left:0;width:674px;height:22px;font-size:8px;color:var(--ink-light);display:flex;justify-content:space-between;align-items:center;padding:0 40px}
.top-strip span{display:flex;align-items:center;gap:4px}

/* header */
.brand{top:26px;left:40px;font-size:24px;font-weight:300;color:var(--gold);letter-spacing:.2px}
.call{top:28px;right:40px;display:flex;align-items:center;gap:8px}
.call-ring{width:30px;height:30px;border:1.5px solid var(--gold);border-radius:50%;display:flex;align-items:center;justify-content:center}
.call small{display:block;font-size:8px;color:var(--ink-light)}
.call strong{font-size:16px;font-weight:500;color:var(--gold)}

/* nav */
.main-nav{top:80px;left:0;width:674px;height:22px;background:var(--gold);display:flex;padding-left:40px}
.main-nav a{font-size:9.5px;color:var(--white);text-decoration:none;text-transform:uppercase;padding:0 16px;line-height:22px}
.main-nav a.active{background:var(--gold-dark)}

/* hero */
.hero{top:102px;left:0;width:674px;height:332px;background:linear-gradient(100deg,#fbf8f2 0%,#f3ece0 38%,#d9c7ab 62%,#c6ad8a 80%,#e8e1d6 100%)}
.hero-title{top:165px;left:40px;width:260px;font-size:26px;font-weight:300;line-height:1.22;color:var(--gold)}
.btn{display:inline-block;background:var(--gold);color:var(--white);font-size:9.5px;text-transform:uppercase;padding:8px 12px}
.hero-btn{top:300px;left:40px}

/* welcome */
.portrait{top:460px;left:42px;width:145px;height:145px;border-radius:50%;border:4px solid var(--white);box-shadow:0 0 0 1px #ddd;background:radial-gradient(circle at 50% 40%,#e9d9c0,#c4a985 60%,#8a9aa5)}
.welcome-title{top:462px;left:206px;font-size:22px;font-weight:400;color:var(--gold)}
.welcome-text{top:494px;left:206px;width:420px;font-size:8px;line-height:1.55;color:var(--ink-light)}
.welcome-btn{top:590px;left:206px}

/* expertise */
.expertise{top:632px;left:0;width:674px;height:230px;background:var(--band)}
.section-title{top:662px;left:0;width:674px;text-align:center;font-size:21px;font-weight:400;color:var(--ink)}
.section-rule{top:695px;left:260px;width:154px;height:1px;background:#ccc}
.skills{top:718px;left:28px;width:618px;display:flex;justify-content:space-between}
.skill{width:118px;text-align:center;font-size:9.5px;color:var(--ink);line-height:1.35}
.skill-ring{width:44px;height:44px;margin:0 auto 10px;border:1.5px solid var(--gold);border-radius:50%;display:flex;align-items:center;justify-content:center}

/* lower columns */
.col-title{font-size:15px;font-weight:400;color:var(--gold)}
.video{top:905px;left:40px;width:180px;height:125px;background:linear-gradient(135deg,#b8c3cc,#e6d6bd 55%,#c9ad88)}
.play{top:952px;left:114px}
.radio-text{top:905px;left:252px;width:180px;font-size:8px;line-height:1.5;color:var(--ink-light)}
.player{top:938px;left:252px;width:185px;height:70px;border:1px solid #ddd;background:#fafafa;padding:6px}
.player-logo{width:22px;height:22px;border-radius:50%;background:var(--gold-soft);float:left;margin-right:6px}
.player b{display:block;font-size:7.5px;font-weight:500;color:var(--ink)}
.player i{font-style:normal;font-size:7px;color:var(--ink-light)}
.wave{position:absolute;left:6px;right:6px;bottom:10px;height:20px;display:flex;align-items:flex-end;gap:1px}
.wave span{flex:1;background:#ccc}
.donate-text{top:905px;left:462px;font-size:8px;color:var(--ink-light)}
.charity{left:462px;width:180px;display:flex;align-items:center;gap:10px}
.badge{width:54px;height:34px;background:var(--gold-soft);border-radius:4px}
.charity-name{font-size:9.5px;color:var(--ink)}
.donate-link{display:flex;align-items:center;gap:4px;font-size:8.5px;color:var(--gold);margin-top:3px}

/* footer */
.footer{top:1070px;left:0;width:674px;height:130px;background:var(--gold);color:var(--white)}
.foot-nav{top:1095px;left:40px;display:flex;gap:20px;font-size:9px}
.social{top:1086px;right:40px;display:flex;gap:10px}
.social span{width:26px;height:26px;border:1.5px solid var(--white);border-radius:50%;display:flex;align-items:center;justify-content:center;font-size:9px;font-weight:500}
.foot-rule{top:1128px;left:40px;width:594px;height:1px;background:rgba(255,255,255,.4)}
.foot-info{top:1140px;left:40px;width:594px;display:flex;justify-content:space-between;font-size:8px;line-height:1.45}
.foot-info div{display:flex;align-items:center;gap:6px}
.foot-info strong{font-size:11px;font-weight:500}
.ico{width:22px;height:22px;border-radius:50%;background:var(--white);display:flex;align-items:center;justify-content:center;flex:none}
</style>
</head>
<body>
<div class="page">

  <div class="abs top-strip">
    <span><svg width="8" height="10" viewBox="0 0 8 10"><path d="M4 0a3.5 3.5 0 0 0-3.5 3.5C.5 6 4 10 4 10s3.5-4 3.5-6.5A3.5 3.5 0 0 0 4 0z" fill="#c9b04c"/><circle cx="4" cy="3.5" r="1.3" fill="#fff"/></svg>418 Linden Row, Suite 120 Harbor Bay, CA 90000</span>
    <span><svg width="10" height="8" viewBox="0 0 10 8"><rect x=".5" y=".5" width="9" height="7" fill="none" stroke="#c9b04c"/><path d="M.5.5 5 4.5 9.5.5" fill="none" stroke="#c9b04c"/></svg>info@drquorvat.com</span>
  </div>

  <div class="abs brand">Dr. Marla Q. Quorvat</div>
  <div class="abs call">
    <div class="call-ring"><svg width="14" height="14" viewBox="0 0 24 24"><path d="M6.6 10.8a15 15 0 0 0 6.6 6.6l2.2-2.2a1 1 0 0 1 1-.25 11.4 11.4 0 0 0 3.6.57 1 1 0 0 1 1 1V20a1 1 0 0 1-1 1A17 17 0 0 1 3 4a1 1 0 0 1 1-1h3.5a1 1 0 0 1 1 1c0 1.25.2 2.45.57 3.57a1 1 0 0 1-.25 1z" fill="#c9b04c"/></svg></div>
    <div><small>Call us now</small><strong>(555) 203 4418</strong></div>
  </div>

  <nav class="abs main-nav">
    <a class="active" href="#">Home</a><a href="#">About</a><a href="#">Sessions</a><a href="#">Resources</a><a href="#">Bio</a><a href="#">Contact</a>
  </nav>

  <div class="abs hero" role="img" aria-label="Photo of a smiling couple embracing on a sunny beach"></div>
  <h1 class="abs hero-title">Your life can be difficult but also possibly life changing.</h1>
  <a class="abs btn hero-btn" href="#">Contact us now</a>

  <div class="abs portrait" role="img" aria-label="Portrait photo of the psychologist"></div>
  <h2 class="abs welcome-title">WELCOME TO Dr. Marla Q. Quorvat</h2>
  <p class="abs welcome-text">I'm so glad you are here. Choosing to see a professional for issues in your life can be difficult but also possibly life changing. Many people seeking help hesitate because they believe asking for support is a weakness. Really? We seek the help of experts all the time: contractors, mechanics, chefs, etc. And what is more important than your life? Consulting with a neutral party to act in your best interest can be time well spent. So if you are willing to take the time to invest in counseling, make sure that it is with someone that is worth your time.</p>
  <a class="abs btn welcome-btn" href="#">Read more</a>

  <section class="abs expertise"></section>
  <h2 class="abs section-title">OUR EXPERTISE</h2>
  <div class="abs section-rule"></div>
  <div class="abs skills">
    <div class="skill"><div class="skill-ring"><svg width="22" height="20" viewBox="0 0 24 22"><path d="M12 21s-9-6-9-12a5 5 0 0 1 9-3 5 5 0 0 1 9 3c0 6-9 12-9 12z" fill="#c9b04c"/></svg></div>Dating, Marriage</div>
    <div class="skill"><div class="skill-ring"><svg width="24" height="22" viewBox="0 0 24 22"><circle cx="7" cy="5" r="3" fill="#c9b04c"/><circle cx="17" cy="5" r="3" fill="#c9b04c"/><path d="M2 20v-7a3 3 0 0 1 3-3h4a3 3 0 0 1 3 3v7zM12 20v-7a3 3 0 0 1 3-3h4a3 3 0 0 1 3 3v7z" fill="#c9b04c"/></svg></div>Parenting &amp; Professional Relationship</div>
    <div class="skill"><div class="skill-ring"><svg width="22" height="22" viewBox="0 0 24 24"><path d="M4 4h16v11H9l-5 4z" fill="none" stroke="#c9b04c" stroke-width="2" stroke-linejoin="round"/><path d="M8 9h8M8 12h5" stroke="#c9b04c" stroke-width="2"/></svg></div>Depression &amp; Anxiety Issues</div>
    <div class="skill"><div class="skill-ring"><svg width="22" height="22" viewBox="0 0 24 24"><path d="M8 21v-4H6a2 2 0 0 1-2-2v-3l-2-1 2-3a8 8 0 0 1 16 2c0 3-1 5-3 6v5" fill="none" stroke="#c9b04c" stroke-width="2" stroke-linejoin="round"/></svg></div>Personality Disorders</div>
    <div class="skill"><div class="skill-ring"><svg width="22" height="22" viewBox="0 0 24 24"><circle cx="12" cy="12" r="9" fill="none" stroke="#c9b04c" stroke-width="2"/><path d="M12 7v5l4 2" fill="none" stroke="#c9b04c" stroke-width="2" stroke-linecap="round"/></svg></div>Life Management</div>
  </div>

  <h3 class="abs col-title" style="top:875px;left:40px">Dr. Marla Q. Quorvat</h3>
  <div class="abs video" role="img" aria-label="Video still of the psychologist speaking"></div>
  <svg class="abs play" width="32" height="32" viewBox="0 0 32 32"><circle cx="16" cy="16" r="15" fill="#c9b04c"/><path d="M13 10l9 6-9 6z" fill="#fff"/></svg>

  <h3 class="abs col-title" style="top:875px;left:252px">Radio Conversation</h3>
  <p class="abs radio-text">Short weekly talks on stress, couples and finding calm in daily life.</p>
  <div class="abs player">
    <div class="player-logo"></div>
    <b>Velvet Tide Hour</b><i>Episode 12: Calm at home</i>
    <div class="wave"><span style="height:40%"></span><span style="height:70%"></span><span style="height:55%"></span><span style="height:90%"></span><span style="height:45%"></span><span style="height:65%"></span><span style="height:80%"></span><span style="height:35%"></span><span style="height:60%"></span><span style="height:95%"></span><span style="height:50%"></span><span style="height:70%"></span><span style="height:40%"></span><span style="height:85%"></span><span style="height:55%"></span><span style="height:65%"></span><span style="height:30%"></span><span style="height:75%"></span><span style="height:50%"></span><span style="height:60%"></span><span style="height:45%"></span><span style="height:80%"></span><span style="height:35%"></span><span style="height:55%"></span><span style="height:70%"></span><span style="height:40%"></span><span style="height:60%"></span><span style="height:50%"></span></div>
  </div>

  <h3 class="abs col-title" style="top:875px;left:462px">Donate to</h3>
  <p class="abs donate-text">A portion of all revenue is donated to</p>
  <div class="abs charity" style="top:928px">
    <div class="badge"></div>
    <div><div class="charity-name">Amber Hollow</div><div class="donate-link"><svg width="10" height="10" viewBox="0 0 10 10"><rect width="10" height="10" rx="2" fill="#c9b04c"/><path d="M3 5l1.5 1.5L7 3.5" stroke="#fff" fill="none"/></svg>DONATE</div></div>
  </div>
  <div class="abs charity" style="top:984px">
    <div class="badge"></div>
    <div><div class="charity-name">Cedar Haven</div><div class="donate-link"><svg width="10" height="10" viewBox="0 0 10 10"><rect width="10" height="10" rx="2" fill="#c9b04c"/><path d="M3 5l1.5 1.5L7 3.5" stroke="#fff" fill="none"/></svg>DONATE</div></div>
  </div>

  <footer class="abs footer"></footer>
  <div class="abs foot-nav"><span>Home</span><span>About</span><span>Sessions</span><span>Resources</span><span>Bio</span><span>Contact</span></div>
  <div class="abs social"><span>B</span><span>C</span><span>K</span></div>
  <div class="abs foot-rule"></div>
  <div class="abs foot-info">
    <div><span class="ico"><svg width="8" height="10" viewBox="0 0 8 10"><path d="M4 0a3.5 3.5 0 0 0-3.5 3.5C.5 6 4 10 4 10s3.5-4 3.5-6.5A3.5 3.5 0 0 0 4 0z" fill="#c9b04c"/></svg></span><span>418 Linden Row, Suite 120<br>Harbor Bay,<br>CA 90000</span></div>
    <div><span class="ico"><svg width="10" height="10" viewBox="0 0 24 24"><path d="M6.6 10.8a15 15 0 0 0 6.6 6.6l2.2-2.2a1 1 0 0 1 1-.25 11.4 11.4 0 0 0 3.6.57 1 1 0 0 1 1 1V20a1 1 0 0 1-1 1A17 17 0 0 1 3 4a1 1 0 0 1 1-1h3.5a1 1 0 0 1 1 1c0 1.25.2 2.45.57 3.57a1 1 0 0 1-.25 1z" fill="#c9b04c"/></svg></span><strong>(555) 203 4418</strong></div>
    <div><span class="ico"><svg width="10" height="8" viewBox="0 0 10 8"><rect x=".5" y=".5" width="9" height="7" fill="none" stroke="#c9b04c"/><path d="M.5.5 5 4.5 9.5.5" fill="none" stroke="#c9b04c"/></svg></span><span>info@drquorvat.com</span></div>
    <div><span class="ico"><svg width="10" height="10" viewBox="0 0 10 10"><circle cx="5" cy="5" r="4" fill="none" stroke="#c9b04c"/></svg></span><span>© DR.QUORVAT, 2016.<br>All Rights Reserved.</span></div>
  </div>

</div>
</body>
</html>
```